Business Card for bespoke luxury cupcakes and cakes
childrens parties, baby showers, seasonal designs, christenings, 3D and 2D designs
Bright & Fun-filled
Tumble Bakes Ltd
London
morvenaltoski@mailnest.co.uk
www.pagelink.co.uk/TumbleBakesLtd

```html
<!DOCTYPE html>
<html lang="en">
<head>
<meta charset="utf-8">
<title>Tumble Bakes Ltd — Stationery Set</title>
<link rel="stylesheet" href="https://fonts.googleapis.com/css2?family=Nunito:wght@400;700;900&display=swap">
<style>
  :root {
    --bg: #2b2727;
    --paper: #ffffff;
    --pink: #e9579b;
    --pink-soft: #f6a9cb;
    --pink-pale: #fbe1ee;
    --ink: #5a4a52;
    --line: #d9c6cf;
    --photo: #b59a86;
  }
  * { box-sizing: border-box; margin: 0; padding: 0; }
  html, body { width: 1200px; height: 883px; overflow: hidden; }
  body { background: var(--bg); font-family: "Nunito", sans-serif; color: var(--ink); position: relative; }

  .sheet { position: absolute; background: var(--paper); overflow: hidden; }
  .band { position: absolute; left: 0; right: 0; bottom: 0; background: linear-gradient(90deg, var(--pink), var(--pink-soft)); }

  .brand { font-weight: 900; color: var(--pink); line-height: 1; display: flex; align-items: center; gap: 5px; white-space: nowrap; }
  .brand .mark { width: 9px; height: 9px; border-radius: 50%; background: var(--pink); flex: none; }

  .contact { font-size: 7px; line-height: 1.55; color: var(--ink); }
  .contact li { list-style: none; display: flex; align-items: center; gap: 4px; white-space: nowrap; }
  .contact svg { width: 7px; height: 7px; flex: none; fill: var(--pink); }

  .artwork { position: absolute; background: radial-gradient(circle at 45% 40%, #fde6c8 0%, var(--pink-soft) 45%, var(--pink) 100%); border-radius: 40% 45% 35% 50%; }
  .photo { background: linear-gradient(135deg, #cdb49d, var(--photo) 60%, #8c7464); border: 3px solid #fff; box-shadow: 0 0 0 1px var(--line); }

  /* Invoice */
  .invoice { left: 40px; top: 40px; width: 300px; height: 424px; }
  .invoice .brand { position: absolute; left: 18px; top: 18px; font-size: 16px; }
  .invoice .contact { position: absolute; right: 16px; top: 16px; font-size: 6px; }
  .invoice .fax { position: absolute; right: 18px; top: 68px; font-size: 9px; font-weight: 900; color: var(--ink); }
  .invoice-table { position: absolute; left: 18px; top: 84px; width: 264px; border-collapse: collapse; font-size: 6.5px; }
  .invoice-table th, .invoice-table td { border: 1px solid var(--line); padding: 3px 4px; text-align: left; height: 14px; }
  .invoice-table th { background: var(--pink-pale); color: var(--pink); font-weight: 700; }
  .invoice-table .total td { font-weight: 700; }
  .invoice .band { height: 14px; }

  /* Letterhead */
  .letterhead { left: 370px; top: 40px; width: 300px; height: 424px; }
  .letterhead .brand { position: absolute; right: 18px; top: 20px; font-size: 16px; }
  .letterhead .contact { position: absolute; right: 18px; top: 44px; font-size: 6px; }
  .letterhead .contact li { justify-content: flex-end; }
  .letterhead .band { height: 14px; }

  /* Envelope */
  .envelope { left: 700px; top: 40px; width: 460px; height: 230px; }
  .envelope .flap { position: absolute; left: 0; top: 0; width: 460px; height: 150px; }
  .envelope .artwork { left: 205px; top: 70px; width: 50px; height: 50px; border-radius: 50%; border: 2px solid #fff; }

  /* Compliment slip */
  .slip { left: 700px; top: 294px; width: 460px; height: 170px; }
  .slip .brand { position: absolute; left: 20px; top: 18px; font-size: 18px; }
  .slip .contact { position: absolute; left: 20px; top: 44px; }
  .slip .greeting { position: absolute; left: 20px; top: 92px; font-size: 11px; font-weight: 700; color: var(--pink); }
  .slip .artwork { right: 28px; top: 38px; width: 86px; height: 100px; }
  .slip .band { height: 14px; }

  /* Business cards */
  .card { width: 340px; height: 196px; border-radius: 8px; }
  .card-front { left: 250px; top: 600px; }
  .card-front .brand { position: absolute; left: 20px; top: 22px; font-size: 24px; }
  .card-front .contact { position: absolute; left: 20px; top: 70px; font-size: 8px; }
  .card-front .artwork { right: 22px; top: 26px; width: 110px; height: 130px; }
  .card-front .band { height: 16px; }

  .card-back { left: 610px; top: 600px; background: var(--pink-pale); }
  .card-back .brand { position: absolute; left: 20px; top: 20px; font-size: 20px; }
  .card-back .photos { position: absolute; left: 20px; top: 62px; display: flex; gap: 12px; }
  .card-back .photo { width: 90px; height: 86px; }
  .card-back .band { height: 16px; }
</style>
</head>
<body>

<!-- Invoice -->
<section class="sheet invoice">
  <div class="brand"><span class="mark"></span>Tumble Bakes</div>
  <ul class="contact">
    <li><svg viewBox="0 0 10 10"><path d="M5 0a3.5 3.5 0 0 0-3.5 3.5C1.5 6 5 10 5 10s3.5-4 3.5-6.5A3.5 3.5 0 0 0 5 0z"/></svg>London</li>
    <li><svg viewBox="0 0 10 10"><rect x="0" y="2" width="10" height="6" rx="1"/></svg>morvenaltoski@mailnest.co.uk</li>
    <li><svg viewBox="0 0 10 10"><circle cx="5" cy="5" r="4.5"/></svg>www.pagelink.co.uk/TumbleBakesLtd</li>
  </ul>
  <div class="fax">FAX</div>
  <table class="invoice-table">
    <tr><th colspan="2">Bill To</th><th>Date</th><th>Invoice No</th></tr>
    <tr><td colspan="2"></td><td></td><td></td></tr>
    <tr><th>Description</th><th>Qty</th><th colspan="2">Amount</th></tr>
    <tr><td></td><td></td><td colspan="2"></td></tr>
    <tr><td></td><td></td><td colspan="2"></td></tr>
    <tr><td></td><td></td><td colspan="2"></td></tr>
    <tr><td></td><td></td><td colspan="2"></td></tr>
    <tr><td></td><td></td><td colspan="2"></td></tr>
    <tr class="total"><td colspan="2"></td><td>Total</td><td></td></tr>
  </table>
  <div class="band"></div>
</section>

<!-- Letterhead -->
<section class="sheet letterhead">
  <div class="brand"><span class="mark"></span>Tumble Bakes</div>
  <ul class="contact">
    <li>London<svg viewBox="0 0 10 10"><path d="M5 0a3.5 3.5 0 0 0-3.5 3.5C1.5 6 5 10 5 10s3.5-4 3.5-6.5A3.5 3.5 0 0 0 5 0z"/></svg></li>
    <li>morvenaltoski@mailnest.co.uk<svg viewBox="0 0 10 10"><rect x="0" y="2" width="10" height="6" rx="1"/></svg></li>
    <li>www.pagelink.co.uk/TumbleBakesLtd<svg viewBox="0 0 10 10"><circle cx="5" cy="5" r="4.5"/></svg></li>
  </ul>
  <div class="band"></div>
</section>

<!-- Envelope -->
<section class="sheet envelope">
  <svg class="flap" viewBox="0 0 460 150" aria-hidden="true">
    <defs>
      <linearGradient id="flapFill" x1="0" x2="1">
        <stop offset="0" stop-color="#e9579b"/>
        <stop offset="1" stop-color="#f6a9cb"/>
      </linearGradient>
    </defs>
    <path d="M0 0H460V40Q340 120 230 140Q120 120 0 40Z" fill="url(#flapFill)"/>
  </svg>
  <div class="artwork" role="img" aria-label="Cartoon cupcake mascot illustration"></div>
</section>

<!-- Compliment slip -->
<section class="sheet slip">
  <div class="brand"><span class="mark"></span>Tumble Bakes</div>
  <ul class="contact">
    <li><svg viewBox="0 0 10 10"><path d="M5 0a3.5 3.5 0 0 0-3.5 3.5C1.5 6 5 10 5 10s3.5-4 3.5-6.5A3.5 3.5 0 0 0 5 0z"/></svg>London</li>
    <li><svg viewBox="0 0 10 10"><rect x="0" y="2" width="10" height="6" rx="1"/></svg>morvenaltoski@mailnest.co.uk</li>
    <li><svg viewBox="0 0 10 10"><circle cx="5" cy="5" r="4.5"/></svg>www.pagelink.co.uk/TumbleBakesLtd</li>
  </ul>
  <div class="greeting">With Compliments</div>
  <div class="artwork" role="img" aria-label="Cartoon cupcake mascot carrying a stack of cakes"></div>
  <div class="band"></div>
</section>

<!-- Business card front -->
<section class="sheet card card-front">
  <div class="brand"><span class="mark"></span>Tumble Bakes</div>
  <ul class="contact">
    <li><svg viewBox="0 0 10 10"><path d="M5 0a3.5 3.5 0 0 0-3.5 3.5C1.5 6 5 10 5 10s3.5-4 3.5-6.5A3.5 3.5 0 0 0 5 0z"/></svg>London</li>
    <li><svg viewBox="0 0 10 10"><rect x="0" y="2" width="10" height="6" rx="1"/></svg>morvenaltoski@mailnest.co.uk</li>
    <li><svg viewBox="0 0 10 10"><circle cx="5" cy="5" r="4.5"/></svg>www.pagelink.co.uk/TumbleBakesLtd</li>
  </ul>
  <div class="artwork" role="img" aria-label="Cartoon cupcake mascot illustration"></div>
  <div class="band"></div>
</section>

<!-- Business card back -->
<section class="sheet card card-back">
  <div class="brand"><span class="mark"></span>Tumble Bakes</div>
  <div class="photos">
    <div class="photo" role="img" aria-label="Photo of decorated cupcakes"></div>
    <div class="photo" role="img" aria-label="Photo of a celebration cake"></div>
    <div class="photo" role="img" aria-label="Photo of seasonal cupcakes"></div>
  </div>
  <div class="band"></div>
</section>

</body>
</html>
```